High Quality fast food restaurant - Tomanyo

Tomanyo is a fast food company with its target's focused on logistic, simplicity, high quality, freshness and modern.

We need a web design where the customers can get a complete idea of our high quality completeness, we want to take fast food to a new upper level.

We would like to see the colours of wood and metal. Pictures have been attached of our local.

We would like to have something in similar to: http://www.qpz.example/
Updates

Images for the food we are going to sell can be found here: http://shrt.example/uWQa7

It will be the images with rice, french fries or pita bread.

Target Market(s)

The fast food eating people between sloppy food and restaurant level.

Industry/Entity Type

Fast Food Restaurant

Requirements
Should not have
• No Flash or Java

```html
<!DOCTYPE html>
<html lang="en">
<head>
<meta charset="utf-8">
<title>Tomanyo – High Quality Fastfood</title>
<link rel="stylesheet" href="https://fonts.googleapis.com/css2?family=Tinos:wght@400;700&family=Arimo:wght@400&display=swap">
<style>
  :root {
    --wood-dark: #1f0f0c;
    --wood-mid: #2e1713;
    --wood-light: #3a1f1a;
    --metal-top: #efe9ec;
    --metal-mid: #d7cdd2;
    --metal-bottom: #b9adb3;
    --nav-divider: #a89ca2;
    --nav-text: #2a2a2a;
    --text-light: #f4efec;
    --text-body: #ece4e0;
    --rule: #3d302d;
    --footer-bg: #2a1e1d;
    --frame: #3b2c29;
  }
  * { margin: 0; padding: 0; box-sizing: border-box; }
  html, body {
    width: 1085px;
    height: 1200px;
    overflow: hidden;
  }
  body {
    position: relative;
    background:
      repeating-linear-gradient(90deg, rgba(255,255,255,0.015) 0 3px, rgba(0,0,0,0.03) 3px 9px, rgba(255,255,255,0.01) 9px 14px),
      linear-gradient(90deg, var(--wood-dark), var(--wood-mid) 35%, var(--wood-light) 55%, var(--wood-mid) 75%, var(--wood-dark));
    font-family: "Tinos", "Times New Roman", serif;
    color: var(--text-body);
  }
  .site-header {
    position: absolute;
    left: 0; top: 0;
    width: 1085px; height: 108px;
    border-bottom: 3px solid #140907;
  }
  .brand-name {
    position: absolute;
    left: 36px; top: 26px;
    font-family: "Tinos", "Times New Roman", serif;
    font-weight: 700;
    font-size: 50px;
    line-height: 1;
    color: #ffffff;
  }
  .main-nav {
    position: absolute;
    left: 0; top: 108px;
    width: 1085px; height: 42px;
    background: linear-gradient(180deg, var(--metal-top), var(--metal-mid) 55%, var(--metal-bottom));
    box-shadow: 0 2px 4px rgba(0,0,0,0.5);
  }
  .nav-list {
    position: absolute;
    left: 264px; top: 0;
    display: flex;
    list-style: none;
    height: 42px;
    border-left: 1px solid var(--nav-divider);
  }
  .nav-list li {
    width: 111px;
    height: 42px;
    border-right: 1px solid var(--nav-divider);
    text-align: center;
    font-family: "Arimo", Arial, sans-serif;
    font-size: 20px;
    line-height: 42px;
    color: var(--nav-text);
  }
  .hero-photo {
    position: absolute;
    left: 0; top: 150px;
    width: 1085px; height: 517px;
    background:
      radial-gradient(ellipse at 55% 50%, #c9a06a 0%, #a9794a 30%, transparent 60%),
      linear-gradient(90deg, #d9a248 0%, #b88a52 30%, #8a6a48 60%, #5b3a28 85%, #3a2117 100%);
    border-bottom: 3px solid #140907;
  }
  .intro {
    position: absolute;
    left: 36px; top: 704px;
    width: 606px;
  }
  .intro-title {
    font-weight: 700;
    font-size: 26px;
    letter-spacing: 0.5px;
    color: var(--text-light);
    padding-bottom: 14px;
    border-bottom: 3px solid var(--rule);
  }
  .intro-text {
    margin-top: 24px;
    font-size: 17px;
    line-height: 22.5px;
    color: var(--text-body);
  }
  .location {
    position: absolute;
    left: 686px; top: 712px;
    width: 362px;
  }
  .location-caption {
    text-align: center;
    font-size: 18px;
    color: var(--text-light);
    margin-bottom: 18px;
  }
  .location-photo {
    width: 362px; height: 363px;
    border: 3px solid var(--frame);
    background: linear-gradient(180deg, #3c2620 0%, #2a1a16 28%, #d8d2cc 30%, #bdb6b0 40%, #1c1616 48%, #0e0c0c 85%, #2a1c18 100%);
  }
  .site-footer {
    position: absolute;
    left: 0; top: 1156px;
    width: 1085px; height: 44px;
    background: var(--footer-bg);
    text-align: center;
    font-size: 15px;
    line-height: 44px;
    color: var(--text-body);
  }
</style>
</head>
<body>
  <header class="site-header">
    <div class="brand-name">TOMANYO</div>
  </header>

  <nav class="main-nav">
    <ul class="nav-list">
      <li>Link 1</li>
      <li>Link 2</li>
      <li>Link 3</li>
      <li>Link 4</li>
      <li>Link 5</li>
    </ul>
  </nav>

  <div class="hero-photo" role="img" aria-label="Pita wrap filled with grilled chicken, lettuce, tomato, onion and feta beside french fries on paper over a wooden board"></div>

  <section class="intro">
    <h1 class="intro-title">High Quality Fastfood</h1>
    <p class="intro-text">Lorem ipsum dolor sit amet, consectetur adipisicing elit, sed do eiusmod tempor incididunt ut labore et dolore magna aliqua. Ut enim ad minim veniam, quis nostrud exercitation ullamco laboris nisi ut aliquip ex ea commodo consequat. Duis aute irure dolor in reprehenderit in voluptate velit esse cillum dolore eu fugiat nulla pariatur. Excepteur sint occaecat cupidatat non proident, sunt in culpa qui officia deserunt mollit anim id est laborum.</p>
  </section>

  <aside class="location">
    <p class="location-caption">Located inside lorem ipsum food court</p>
    <div class="location-photo" role="img" aria-label="Storefront of the restaurant counter inside a food court, with wooden signboard and lit menu panels"></div>
  </aside>

  <footer class="site-footer">Copyright © Tomanyo, All Rights Reserved.</footer>
</body>
</html>
```